Brava Stone Oven Kitchen (restaurant)

Restaurant with a cool vibe.
We need a refresh of existing site. Appealing to a hip crowd of 25 or older age bracket (mid price to high small town). Constant changes food and cocktail menu. A vibing atmosphere with jazz funk hip music.
Must be able to scale for any device… phone/mobile device super important.
Instagram: @Brava.Linwell
Website: bravalinwell.example

Target Market(s)

25-55 age group

Number of Pages Required

1 page

Font styles to use
Sans Serif

Requirements
Must have
• Simple to navigate. Simplicity is the key to all sophistication.

Links/Buttons
Menu
Gift Cards
Reservations
Take Out
Contact Us
Should not have
• Please, nothing generic looking… no cookie cutter look. Originality

```html
<!DOCTYPE html>
<html lang="en">
<head>
<meta charset="utf-8">
<title>Brava Stone Oven Kitchen</title>
<link rel="stylesheet" href="https://fonts.googleapis.com/css2?family=Delius&family=Nunito+Sans:wght@400;600;800&display=swap">
<style>
  :root {
    --cream: #e9e4df;
    --cream-band: #ddd5cd;
    --brown: #6a3504;
    --ink: #2a1a0e;
    --footer: #2b1508;
    --footer-base: #24140b;
    --footer-text: #efe7de;
    --tile-edge: #7a3f12;
    --display: "Delius", sans-serif;
    --sans: "Nunito Sans", sans-serif;
  }
  * { box-sizing: border-box; margin: 0; padding: 0; }
  html, body { width: 1011px; height: 1200px; overflow: hidden; background: var(--cream); }
  body { position: relative; font-family: var(--sans); color: var(--ink); }

  .hero { position: absolute; left: 0; top: 0; width: 1011px; height: 489px; }
  .hero-photo { position: absolute; top: 0; height: 489px; width: 337px; }
  .hero-photo--left {
    left: 0;
    background:
      radial-gradient(ellipse 60% 30% at 50% 20%, rgba(240,140,110,.55), transparent 70%),
      radial-gradient(ellipse 70% 40% at 40% 70%, rgba(230,110,80,.6), transparent 70%),
      linear-gradient(180deg, #9a4a32 0%, #5a2a1c 38%, #c1573d 55%, #b2462f 100%);
  }
  .hero-photo--right {
    left: 674px;
    background:
      radial-gradient(ellipse 25% 30% at 80% 20%, rgba(255,190,90,.7), transparent 70%),
      radial-gradient(ellipse 60% 25% at 35% 82%, rgba(220,110,80,.6), transparent 70%),
      linear-gradient(180deg, #6a2a18 0%, #a0533a 40%, #b96a48 65%, #9a4530 100%);
  }

  .panel { position: absolute; left: 337px; top: 0; width: 337px; height: 489px; background: var(--cream); text-align: center; }
  .brand { position: absolute; left: 0; right: 0; top: 28px; color: var(--brown); font-family: var(--sans); font-weight: 800; line-height: 1; }
  .brand-name { font-size: 30px; letter-spacing: 1px; }
  .brand-sub { font-size: 10px; margin-top: 1px; letter-spacing: .3px; }
  .status { position: absolute; left: 0; right: 0; top: 81px; font-size: 12px; color: var(--brown); letter-spacing: .5px; }

  .nav { position: absolute; left: 0; right: 0; top: 150px; list-style: none; }
  .nav-item { height: 37px; line-height: 37px; font-family: var(--display); font-size: 15px; letter-spacing: 1px; color: var(--ink); position: relative; }
  .nav-item--active { background: var(--cream-band); color: var(--brown); height: 31px; line-height: 31px; margin: 3px 0; }
  .nav-item svg { position: absolute; right: 10px; top: 9px; }

  .order-btn { position: absolute; left: 95px; top: 354px; width: 147px; height: 32px; border-radius: 16px; background: var(--brown); color: #f4ece3; font-family: var(--display); font-size: 13px; letter-spacing: .5px; line-height: 32px; }

  .social { position: absolute; left: 0; right: 0; top: 447px; display: flex; justify-content: center; gap: 28px; }
  .social span { width: 18px; height: 18px; border: 2px solid var(--ink); border-radius: 50%; }

  .gallery { position: absolute; left: 0; top: 489px; width: 1011px; height: 496px; background: linear-gradient(180deg, #e6e0da, #e2dbd4); }
  .gallery-title { position: absolute; left: 0; right: 0; top: 62px; text-align: center; font-family: var(--display); font-size: 23px; letter-spacing: 1px; color: var(--ink); font-weight: 400; }
  .gallery-title em { font-style: normal; color: var(--brown); }
  .tile { position: absolute; border: 1px solid var(--tile-edge); border-radius: 8px; box-shadow: 0 2px 5px rgba(0,0,0,.25); }

  .footer { position: absolute; left: 0; top: 985px; width: 1011px; height: 173px; background: var(--footer); color: var(--footer-text); }
  .hours { position: absolute; left: 42px; top: 28px; }
  .hours h3 { font-family: var(--display); font-weight: 400; font-size: 14px; letter-spacing: .5px; margin-bottom: 4px; }
  .hours .takeout { margin-top: 14px; }
  .hours table { border-collapse: collapse; margin-left: 16px; font-size: 10px; }
  .hours td { padding: 2px 0; height: 16px; }
  .hours td:first-child { width: 106px; }
  .hours small { font-size: 7.5px; text-transform: uppercase; }
  .footer-brand { position: absolute; left: 0; right: 0; top: 68px; text-align: center; color: var(--footer-text); font-weight: 800; line-height: 1; }
  .contact { position: absolute; right: 42px; top: 30px; list-style: none; font-size: 10px; text-align: right; }
  .contact li { display: flex; align-items: center; justify-content: flex-end; gap: 10px; height: 22px; margin-bottom: 8px; }
  .contact li.addr { margin-top: 22px; line-height: 1.3; }

  .legal { position: absolute; left: 0; top: 1158px; width: 1011px; height: 42px; background: var(--footer-base); color: #a89a8c; font-size: 8px; text-align: center; line-height: 42px; }
</style>
</head>
<body>
  <header class="hero">
    <div class="hero-photo hero-photo--left" role="img" aria-label="Close-up of a stone-oven pizza with peppers and cured meat"></div>
    <div class="panel">
      <div class="brand">
        <div class="brand-name">BRAVA</div>
        <div class="brand-sub">Stone Oven Kitchen</div>
      </div>
      <div class="status">OPEN NOW</div>
      <ul class="nav">
        <li class="nav-item">menu</li>
        <li class="nav-item">gift cards</li>
        <li class="nav-item nav-item--active">reservations
          <svg width="8" height="13" viewBox="0 0 8 13"><path d="M1 1l5.5 5.5L1 12" fill="none" stroke="#2a1a0e" stroke-width="2"/></svg>
        </li>
        <li class="nav-item">take out</li>
        <li class="nav-item">contact us</li>
      </ul>
      <div class="order-btn">order online</div>
      <div class="social" aria-label="Social links"><span></span><span></span><span></span></div>
    </div>
    <div class="hero-photo hero-photo--right" role="img" aria-label="Pizza baking beside the open flames of the stone oven"></div>
  </header>

  <section class="gallery">
    <h2 class="gallery-title">Follow us on Instagram <em>@brava.linwell</em></h2>
    <div class="tile" style="left:37px;top:122px;width:147px;height:146px;background:radial-gradient(circle at 30% 45%,#8a8a4a,transparent 45%),radial-gradient(circle at 70% 25%,#d48a4a,transparent 40%),radial-gradient(circle at 70% 80%,#b06a2a,transparent 40%),#4a4a48" role="img" aria-label="Bowls of spiced dips"></div>
    <div class="tile" style="left:195px;top:122px;width:147px;height:146px;background:radial-gradient(ellipse at 50% 50%,#b8b070,transparent 55%),linear-gradient(180deg,#c99a5a,#d9a86a 40%,#8a9a4a 60%,#c08a5a)" role="img" aria-label="Burger with guacamole and greens"></div>
    <div class="tile" style="left:353px;top:122px;width:147px;height:146px;background:linear-gradient(180deg,#6a5a4a 0%,#d8b07a 20%,#e0bb80 35%,#4a2a18 55%,#a05a5a 72%,#6a8a3a 90%)" role="img" aria-label="Roast beef sandwich with onions"></div>
    <div class="tile" style="left:511px;top:122px;width:147px;height:146px;background:radial-gradient(ellipse at 45% 45%,#e0d0b0,#c8a478 60%,#6a3a1a)" role="img" aria-label="Mushroom flatbread with microgreens"></div>
    <div class="tile" style="left:669px;top:122px;width:304px;height:305px;background:linear-gradient(180deg,#9a5a3a 0%,#b0785a 40%,#6a4a3a 52%,#e8dcc4 70%,#e4cfa8 100%)" role="img" aria-label="Guest presenting a plate of tacos"></div>
    <div class="tile" style="left:37px;top:280px;width:305px;height:147px;background:radial-gradient(ellipse at 25% 55%,#a88a5a,transparent 45%),radial-gradient(ellipse at 70% 60%,#b89a6a,transparent 45%),linear-gradient(180deg,#d8cfc0,#5a3a1a 70%,#c06a2a)" role="img" aria-label="Herb-rolled roast pork slices"></div>
    <div class="tile" style="left:353px;top:280px;width:147px;height:147px;background:radial-gradient(ellipse at 50% 60%,#c0a8a0,#9a8c84 50%,#3a302c)" role="img" aria-label="Charcuterie plate with berries"></div>
    <div class="tile" style="left:511px;top:280px;width:147px;height:147px;background:radial-gradient(ellipse at 45% 55%,#e8d070,#b8a070 45%,#6a5a4a)" role="img" aria-label="Pressed ham and cheese sandwich"></div>
  </section>

  <footer class="footer">
    <div class="hours">
      <h3>Outdoor Dining Hours</h3>
      <table>
        <tr><td>Thursday, Sunday:</td><td>12<small>pm</small> to 8<small>pm</small></td></tr>
        <tr><td>Friday, Saturday:</td><td>12<small>pm</small> to late</td></tr>
      </table>
      <h3 class="takeout">Takeout Hours</h3>
      <table>
        <tr><td>Thursday to Sunday:</td><td>12<small>pm</small> to 8<small>pm</small></td></tr>
      </table>
    </div>
    <div class="footer-brand">
      <div class="brand-name">BRAVA</div>
      <div class="brand-sub">Stone Oven Kitchen</div>
    </div>
    <ul class="contact">
      <li>555-014-2290
        <svg width="20" height="20" viewBox="0 0 24 24"><path d="M6 2l3 5-2 2c1 3 4 6 7 7l2-2 5 3-2 4C11 21 3 13 2 4z" fill="#efe7de"/></svg>
      </li>
      <li>hello@bravalinwell.example
        <svg width="22" height="16" viewBox="0 0 22 16"><rect width="22" height="16" rx="1" fill="#efe7de"/><path d="M1 1l10 8 10-8" fill="none" stroke="#2b1508" stroke-width="1.5"/></svg>
      </li>
      <li class="addr"><span>48 Orchard Lane<br>Linwell, ON</span>
        <svg width="20" height="24" viewBox="0 0 20 24"><path d="M0 8l6-2 8 3 6-2v17l-6 2-8-3-6 2z" fill="#efe7de"/><circle cx="10" cy="6" r="5" fill="#efe7de" stroke="#2b1508"/><circle cx="10" cy="6" r="1.8" fill="#2b1508"/></svg>
      </li>
    </ul>
  </footer>
  <div class="legal">© 2021 Brava. Copyright. All Rights Reserved</div>
</body>
</html>
```